"Vine Hollow Excursions" is a top notch Santa Barbara County Wine Tour company.

We provide scenic, boutique and custom wine tours. I need the card to be clean and classy. I will provide our logo. I would like the logo to cover the back side of the card as an option and would like to see a couple color options other then our signature green and gold. I would like to see some creative options and let the designers come up with options.
I need cards for myself and my team. The final design should communicate "An authentic and boutique wine tour experience"
Please use my website for reference www.vinehollowexcursions.example

Target Market(s)

We have a wide range of clients from millennials to baby boomers

Industry/Entity Type

Tour

Contact Information for Business Card

Contact info:
Dale Marsh
805-218-6390
info@vinehollowexcursions.example
vinehollowexcursions.example

Colors

Designer to choose colors to be used in the design.

Requirements
Must have
• my logo
Nice to have
• *I would like to have the backside side with the logo and the company statement
• "An authentic and boutique wine tour experience" as an option.
• *I would also like to see what the designers can create!
• *I would like to see an option that incorporates or social: pixgram, rantly, journey guide
Should not have
• I do not want it too busy.

```html
<!DOCTYPE html>
<html lang="en">
<head>
<meta charset="utf-8">
<title>Vine Hollow Excursions – Business Card</title>
<link rel="stylesheet" href="https://fonts.googleapis.com/css2?family=Noto+Serif:wght@400;700&display=swap">
<style>
  :root {
    --page-bg: #ecebe7;
    --card-bg: #ffffff;
    --brand-green: #1f6b3c;
    --ink: #1a1a1a;
    --muted-ink: #333333;
    --card-shadow: 0 6px 18px rgba(0, 0, 0, 0.12);
  }
  * { box-sizing: border-box; margin: 0; padding: 0; }
  html, body {
    width: 1200px;
    height: 800px;
    overflow: hidden;
    background: var(--page-bg);
    font-family: "Noto Serif", Georgia, serif;
  }
  .canvas {
    position: relative;
    width: 1200px;
    height: 800px;
  }
  .card {
    position: absolute;
    top: 250px;
    width: 525px;
    height: 300px;
    background: var(--card-bg);
    box-shadow: var(--card-shadow);
    overflow: hidden;
  }
  .card--front { left: 50px; }
  .card--back { left: 625px; }

  /* Front: brand name lockup */
  .brand-lockup {
    position: absolute;
    inset: 0;
    display: flex;
    flex-direction: column;
    align-items: center;
    justify-content: center;
    gap: 16px;
  }
  .brand-lockup__mark {
    width: 34px;
    height: 34px;
    background: var(--brand-green);
  }
  .brand-lockup__name {
    font-size: 26px;
    font-weight: 400;
    letter-spacing: 0.06em;
    color: var(--brand-green);
  }

  /* Back: contact details */
  .contact-block {
    position: absolute;
    top: 80px;
    left: 0;
    right: 0;
    display: flex;
    align-items: center;
  }
  .contact-block__name {
    width: 222px;
    padding-left: 46px;
    font-size: 21px;
    font-weight: 700;
    color: var(--brand-green);
    white-space: nowrap;
  }
  .contact-block__divider {
    flex: none;
    width: 2px;
    height: 66px;
    background: var(--brand-green);
  }
  .contact-block__details {
    list-style: none;
    padding-left: 26px;
    font-size: 13px;
    line-height: 1.3;
    color: var(--ink);
    white-space: nowrap;
  }
  .social-row {
    position: absolute;
    bottom: 48px;
    left: 0;
    right: 0;
    display: flex;
    justify-content: center;
    gap: 22px;
    list-style: none;
    font-size: 12px;
    font-weight: 700;
    color: var(--muted-ink);
  }
</style>
</head>
<body>
  <main class="canvas">
    <section class="card card--front" aria-label="Card front">
      <div class="brand-lockup">
        <span class="brand-lockup__mark" aria-hidden="true"></span>
        <span class="brand-lockup__name">Vine Hollow Excursions</span>
      </div>
    </section>

    <section class="card card--back" aria-label="Card back">
      <div class="contact-block">
        <h1 class="contact-block__name">Dale Marsh</h1>
        <span class="contact-block__divider" aria-hidden="true"></span>
        <ul class="contact-block__details">
          <li>805-218-6390</li>
          <li>info@vinehollowexcursions.example</li>
          <li>vinehollowexcursions.example</li>
        </ul>
      </div>
      <ul class="social-row">
        <li>journey guide</li>
        <li>pixgram</li>
        <li>rantly</li>
      </ul>
    </section>
  </main>
</body>
</html>
```